Creative, Fun, Eye catching signage for new office - inspire and inform!

I am looking for a billboard sign, a smaller sign and a very small sign for parking spots. These will be located in our new office space. I have uploaded two logos, this way you can choose. I would love to see what it looks like with black behind the logo but am open to creative ideas. I would like the majority of the background to be black and/or white

1. Sign for over door – with five at the top like in the photo attached

The sign size is 2600mm (L) x 900mm (H)

Logo at the top then services to the right side
Social & Living Skills Programs
Support Workers
Respite/Supported Holidays
Exercise Physiology
Occupational Therapy
Speech Therapy
Psychology
Behavioural Therapy

I would like the design to tie in with the website and/or flyers/banners attached. Please also try and add 1800 527 930

2. Sign for glass roller door

745cm wide by 725cm high ( similar to what next door has without it saying parent )

Tallbrook Logo
Drop Off Zone

Smaller signs for parking spots
1000cm wide, 60cm high

Tallbrook logo Visitor Parking 24/7

I would like the design to be consistent across the three items so they work together but are not identical.

I have attached images showing what I am talking about in relation to the location of each sign.

Target Market(s)

Families, parents and people with disabilities

Industry/Entity Type

Disability and community service

Colors

Designer to choose colors to be used in the design.

Requirements
Must have
• White or black background - the logo and please use colours shown in the brochures and banners provided. Preferences are black white and yellow
Nice to have
• all of our services and website and/or 1800 527 930 on banner 1
Should not have
• I dont want it to be to busy please

```html
<!DOCTYPE html>
<html lang="en">
<head>
<meta charset="utf-8">
<title>Tallbrook Office Signage</title>
<link href="https://fonts.googleapis.com/css2?family=Gochi+Hand&family=Poppins:wght@500;700;800&display=swap" rel="stylesheet">
<style>
  :root {
    --stage: #bcbcbc;
    --ink: #0d0d0d;
    --paper: #ffffff;
    --sun: #fbd633;
    --sky: #4a9bea;
    --rose: #ec4470;
    --label: #1f1f1f;
    --divider: #2f5fbf;
  }
  * { margin: 0; padding: 0; box-sizing: border-box; }
  html, body { width: 840px; height: 1200px; overflow: hidden; }
  body { background: var(--stage); position: relative; font-family: "Poppins", sans-serif; }

  .sign { position: absolute; overflow: hidden; background: var(--paper); box-shadow: 0 3px 6px rgba(0,0,0,.3); }
  .sign svg { position: absolute; inset: 0; }

  .size-label {
    position: absolute; left: 0; width: 840px; text-align: center;
    font: 500 42px/1 "Poppins", sans-serif; color: var(--label);
  }
  .size-label span { display: inline-block; padding-bottom: 4px; border-bottom: 1.5px solid var(--label); }

  .brand-name { position: absolute; font-family: "Gochi Hand", cursive; color: var(--ink); text-align: center; line-height: 1; white-space: nowrap; }
  .brand-dot { position: absolute; border-radius: 50%; background: var(--sun); }

  /* Over-door billboard */
  .billboard { left: 51px; top: 57px; width: 738px; height: 255px; }
  .billboard .brand-dot { left: 174px; top: 19px; width: 54px; height: 54px; }
  .billboard .brand-name { left: 20px; top: 80px; width: 280px; font-size: 62px; letter-spacing: -1px; }
  .tagline { position: absolute; left: 20px; width: 286px; text-align: center; font-family: "Gochi Hand", cursive; line-height: 1; white-space: nowrap; }
  .tagline.lead { top: 160px; font-size: 35px; color: var(--sky); }
  .tagline.sub { top: 199px; font-size: 29px; color: var(--rose); }

  .service { position: absolute; width: 104px; text-align: center; color: var(--paper); font-family: "Gochi Hand", cursive; font-size: 15px; line-height: 15px; white-space: nowrap; }
  .service.top-row { top: 31px; }
  .service.bottom-row { top: 119px; }
  .service-icon { display: block; width: 32px; height: 32px; margin: 0 auto 8px; border: 1.5px solid var(--sun); border-radius: 6px; background: rgba(251,214,51,.12); }
  .col-1 { left: 348px; } .col-2 { left: 453px; } .col-3 { left: 543px; } .col-4 { left: 631px; }

  .phone { position: absolute; left: 371px; top: 205px; display: flex; align-items: center; gap: 14px; }
  .phone-badge { width: 26px; height: 26px; border-radius: 50%; background: var(--rose); display: grid; place-items: center; }
  .phone-number { font: 800 35px/1 "Poppins", sans-serif; color: var(--paper); letter-spacing: 5px; }

  /* Roller door sign */
  .door-sign { left: 232px; top: 454px; width: 376px; height: 365px; }
  .door-sign .brand-dot { left: 193px; top: 20px; width: 52px; height: 52px; }
  .door-sign .brand-name { left: 0; top: 72px; width: 356px; font-size: 60px; }
  .door-title { position: absolute; left: 0; width: 376px; top: 204px; text-align: center; font: 800 56px/52px "Poppins", sans-serif; color: var(--paper); }

  /* Parking strip */
  .parking-strip { left: 67px; top: 1004px; width: 706px; height: 42px; }
  .parking-strip .brand-dot { left: 58px; top: 5px; width: 14px; height: 14px; }
  .parking-strip .brand-name { left: 18px; top: 20px; width: 72px; font-size: 16px; }
  .parking-title { position: absolute; left: 113px; top: 2px; font: 800 37px/42px "Poppins", sans-serif; color: var(--ink); white-space: nowrap; }
  .parking-hours { position: absolute; left: 518px; top: 2px; font: 800 38px/42px "Poppins", sans-serif; letter-spacing: 6px; color: var(--sun); white-space: nowrap; }
</style>
</head>
<body>

  <!-- Over-door billboard -->
  <div class="sign billboard">
    <svg width="738" height="255" viewBox="0 0 738 255">
      <defs>
        <linearGradient id="bbPhoto" x1="0" y1="0" x2="1" y2="1">
          <stop offset="0" stop-color="#1e1a0c"/>
          <stop offset=".5" stop-color="#14120a"/>
          <stop offset="1" stop-color="#0b0a06"/>
        </linearGradient>
      </defs>
      <path d="M352 0 C318 50 306 120 322 175 C330 210 340 235 352 255 L738 255 L738 0 Z" fill="url(#bbPhoto)" role="img" aria-label="Darkened photo of participants enjoying group activities"/>
      <path d="M340 0 C306 55 296 125 312 180 C320 212 330 236 340 255" fill="none" stroke="var(--sun)" stroke-width="4"/>
      <path d="M350 0 C316 55 306 120 320 175" fill="none" stroke="var(--ink)" stroke-width="6"/>
      <path d="M360 0 C334 40 324 80 322 110" fill="none" stroke="var(--sun)" stroke-width="2"/>
      <g stroke="var(--divider)" stroke-width="1" stroke-dasharray="3 2">
        <line x1="343" y1="114" x2="714" y2="114"/>
        <line x1="459" y1="22" x2="459" y2="196"/>
        <line x1="551" y1="22" x2="551" y2="196"/>
        <line x1="640" y1="22" x2="640" y2="196"/>
      </g>
    </svg>
    <div class="brand-dot"></div>
    <div class="brand-name">TALLBROOK</div>
    <div class="tagline lead">More Independence</div>
    <div class="tagline sub">More Choice &amp; More Fun</div>

    <div class="service top-row col-1"><i class="service-icon" role="img" aria-label="Social skills icon"></i>Social &amp; Living<br>Skills Programs</div>
    <div class="service top-row col-2"><i class="service-icon" role="img" aria-label="Support workers icon"></i>Support<br>Workers</div>
    <div class="service top-row col-3"><i class="service-icon" role="img" aria-label="Exercise physiology icon"></i>Exercise<br>Physiology</div>
    <div class="service top-row col-4"><i class="service-icon" role="img" aria-label="Speech therapy icon"></i>Speech<br>Therapy</div>
    <div class="service bottom-row col-1"><i class="service-icon" role="img" aria-label="Holidays icon"></i>Supported /<br>Respite Holidays</div>
    <div class="service bottom-row col-2"><i class="service-icon" role="img" aria-label="Psychology icon"></i>Psychology</div>
    <div class="service bottom-row col-3"><i class="service-icon" role="img" aria-label="Occupational therapy icon"></i>Occupational<br>Therapy</div>
    <div class="service bottom-row col-4"><i class="service-icon" role="img" aria-label="Behavioural therapy icon"></i>Behavioural<br>Therapy</div>

    <div class="phone">
      <span class="phone-badge">
        <svg width="14" height="14" viewBox="0 0 24 24" style="position:static"><path fill="#fff" d="M6.6 10.8a15.1 15.1 0 0 0 6.6 6.6l2.2-2.2c.3-.3.7-.4 1-.2 1.1.4 2.3.6 3.6.6.6 0 1 .4 1 1V20c0 .6-.4 1-1 1A17 17 0 0 1 3 4c0-.6.4-1 1-1h3.5c.6 0 1 .4 1 1 0 1.300.2 2.500.6 3.600.1.300 0 .700-.2 1z"/></svg>
      </span>
      <span class="phone-number">1800 527 930</span>
    </div>
  </div>
  <div class="size-label" style="top:346px"><span>2600 x 600</span></div>

  <!-- Roller door sign -->
  <div class="sign door-sign">
    <svg width="376" height="365" viewBox="0 0 376 365">
      <defs>
        <linearGradient id="doorPhoto" x1="0" y1="0" x2="0" y2="1">
          <stop offset="0" stop-color="#1f1a0b"/>
          <stop offset="1" stop-color="#0c0b07"/>
        </linearGradient>
      </defs>
      <path d="M0 224 C110 150 266 150 376 224 L376 365 L0 365 Z" fill="url(#doorPhoto)" role="img" aria-label="Darkened photo of participants in wheelchairs outdoors"/>
      <path d="M0 210 C110 135 266 135 376 210" fill="none" stroke="var(--sun)" stroke-width="5"/>
      <path d="M0 218 C110 146 266 146 376 218" fill="none" stroke="var(--ink)" stroke-width="6"/>
      <path d="M60 176 C140 146 240 146 320 176" fill="none" stroke="var(--sun)" stroke-width="2"/>
    </svg>
    <div class="brand-dot"></div>
    <div class="brand-name">TALLBROOK</div>
    <div class="door-title">DROP OFF<br>ZONE</div>
  </div>
  <div class="size-label" style="top:867px"><span>745 x 725</span></div>

  <!-- Parking strip -->
  <div class="sign parking-strip">
    <svg width="706" height="42" viewBox="0 0 706 42">
      <polygon points="505,0 706,0 706,42 487,42" fill="var(--ink)"/>
      <line x1="500" y1="0" x2="482" y2="42" stroke="var(--sun)" stroke-width="3"/>
      <line x1="494" y1="0" x2="476" y2="42" stroke="var(--sun)" stroke-width="1.5"/>
      <circle cx="651" cy="22" r="10" fill="none" stroke="var(--sun)" stroke-width="2" stroke-dasharray="44 19"/>
      <polyline points="651,15 651,22 655,24" fill="none" stroke="var(--sun)" stroke-width="2"/>
    </svg>
    <div class="brand-dot"></div>
    <div class="brand-name">TALLBROOK</div>
    <div class="parking-title">VISITOR PARKING</div>
    <div class="parking-hours">24/7</div>
  </div>
  <div class="size-label" style="top:1086px"><span>1000 x 60</span></div>

</body>
</html>
```